Web Design Project for selling festive lights

I need a modern and easy to navigate website that is going to sell festive lights.
The name of the site will be "fernglow" and the logo can be found in the following link: http://filedrop-example.net/Xq7pRt2Z?
The target group will be people that search for nice decoration lights for their living room, patio and children bedroom.
We need to have a professional look in order to make our webpage distinctive among competition.
The actual products that we are going to sell are cotton ball lights. Pictures can be found in websites like wickandwool.co.uk and many others.
I need to have a design of the homepage, products pages, customer review page, and shopping cart. The design will be "locked" on a php.

Industry/Entity Type

Shopping

Requirements
Must have
• The fonts used in the design must be compatible with the Greek language because that site will be in Greek.
Nice to have
• Flash and non flash banners

```html
<!DOCTYPE html>
<html lang="en">
<head>
<meta charset="utf-8">
<title>fernglow — festive cotton ball lights</title>
<link rel="stylesheet" href="https://fonts.googleapis.com/css2?family=Patrick+Hand&family=Arimo:wght@400;700&display=swap">
<style>
  :root {
    --yellow: #f7d21e;
    --yellow-light: #fde977;
    --yellow-dark: #e8b90c;
    --ink: #454545;
    --text: #444444;
    --muted: #777777;
    --rule: #b9b9b9;
    --accent: #c99a00;
    --field: #e9e9e9;
    --page: #ffffff;
    --social-a: #4a67a8;
    --social-b: #62b8e6;
  }
  * { box-sizing: border-box; margin: 0; padding: 0; }
  html, body { width: 848px; height: 1200px; overflow: hidden; background: var(--page); }
  body { font-family: "Arimo", Arial, sans-serif; color: var(--text); }
  .page { position: relative; width: 848px; height: 1200px; overflow: hidden; }
  .abs { position: absolute; }

  .header-band {
    left: 0; top: 0; width: 848px; height: 85px;
    background: linear-gradient(#e7e7e7, #fafafa);
    border-bottom: 1px solid #d0d0d0;
  }
  .brand {
    left: 62px; top: 5px; width: 194px; height: 115px;
    border-radius: 50%; background: #fff; border: 1px dashed #aaa;
    display: flex; align-items: center; justify-content: center; gap: 8px;
  }
  .brand-dot { width: 14px; height: 14px; border-radius: 50%; background: var(--yellow); }
  .brand-name { font-family: "Patrick Hand", cursive; font-size: 34px; color: #3a3a3a; }

  .lang { top: 14px; right: 66px; font-size: 10px; color: var(--muted); }
  .lang .sep { margin: 0 6px; color: #bbb; }
  .social { top: 35px; right: 65px; display: flex; gap: 2px; }
  .social i {
    display: block; width: 23px; height: 23px; border-radius: 4px;
    border: 1px solid rgba(255,255,255,.7); box-shadow: 0 1px 2px rgba(0,0,0,.25);
  }
  .social .s1 { background: linear-gradient(#6a86c4, var(--social-a)); }
  .social .s2 { background: linear-gradient(#8fd0f2, var(--social-b)); }

  .nav { top: 64px; left: 270px; width: 514px; height: 21px; font-family: "Patrick Hand", cursive; font-size: 13px; color: var(--ink); }
  .nav a { position: absolute; top: 0; height: 21px; line-height: 22px; color: inherit; text-decoration: none; white-space: nowrap; }
  .nav a.active { background: linear-gradient(var(--yellow-light), var(--yellow)); border-radius: 4px 4px 0 0; width: 47px; text-align: center; }

  .search {
    left: 609px; top: 96px; width: 173px; height: 20px;
    border: 1px solid #b5b5b5; border-radius: 4px; background: #fff;
    font-size: 10px; color: #999; padding: 4px 8px; box-shadow: inset 0 1px 2px rgba(0,0,0,.12);
  }
  .search svg { position: absolute; right: 5px; top: 4px; }

  .hero {
    left: 62px; top: 125px; width: 720px; height: 335px; border-radius: 4px;
    background:
      linear-gradient(180deg, rgba(255,255,255,.15), rgba(0,0,0,.04)),
      linear-gradient(100deg, #d3d6dc 0%, #c6cad1 28%, #d9b08a 38%, #f0843a 46%, #ee6a2a 50%, #d98a6a 55%, #c9c4c6 63%, #cdd0d6 78%, #d7d9dd 100%);
  }
  .slide-arrow {
    top: 274px; width: 32px; height: 31px;
    background: linear-gradient(var(--yellow-light), var(--yellow-dark));
    display: flex; align-items: center; justify-content: center;
  }

  .section-title {
    font-family: "Patrick Hand", cursive; font-weight: 400; font-size: 20px; color: var(--ink);
    text-align: center; border-top: 1px solid var(--rule); border-bottom: 1px solid var(--rule);
    height: 36px; line-height: 37px;
  }
  .feature { top: 479px; width: 216px; }
  .feature p { margin-top: 14px; font-size: 9.6px; line-height: 12.8px; text-align: center; white-space: nowrap; }

  .products-title { left: 62px; top: 620px; width: 720px; }
  .products-title svg { position: absolute; top: 10px; }
  .product {
    width: 106px; height: 106px; border: 2px solid #d4d4d4;
    box-shadow: inset 0 0 0 1px #fff;
  }

  .testimonials { left: 62px; top: 938px; width: 326px; }
  .quote { font-size: 9.6px; line-height: 12.8px; text-align: center; white-space: nowrap; }
  .quote cite { display: block; text-align: right; font-style: normal; color: var(--accent); margin-top: 1px; padding-right: 4px; }

  .subscribe { left: 412px; top: 938px; width: 370px; }
  .subscribe-intro { font-size: 9.6px; line-height: 12.8px; text-align: center; margin-top: 19px; }
  .field {
    left: 433px; width: 332px; height: 22px; background: var(--field);
    border: 1px solid #cfcfcf; border-radius: 4px; box-shadow: 1px 2px 2px rgba(0,0,0,.2);
    font-size: 10px; color: #333; padding: 5px 10px;
  }
  .subscribe-btn {
    left: 433px; top: 1116px; width: 75px; height: 21px; border-radius: 3px;
    background: linear-gradient(var(--yellow-light), var(--yellow-dark));
    font-size: 9.6px; font-weight: 700; color: #222; text-align: center; line-height: 21px;
  }

  .footer {
    left: 0; top: 1165px; width: 848px; height: 35px;
    background: linear-gradient(var(--yellow-light), var(--yellow));
    font-size: 8px; color: #222; text-align: center; line-height: 37px;
  }
</style>
</head>
<body>
<div class="page">
  <div class="abs header-band"></div>

  <div class="abs brand"><span class="brand-dot"></span><span class="brand-name">fernglow</span></div>

  <div class="abs lang">English<span class="sep">|</span>Greek</div>
  <div class="abs social" aria-label="Social links"><i class="s1"></i><i class="s2"></i></div>

  <nav class="abs nav">
    <a class="active" style="left:0">HOME</a>
    <a style="left:67px">PRESELECTED</a>
    <a style="left:160px">PICK YOUR OWN</a>
    <a style="left:262px">BIG LAMPS</a>
    <a style="left:342px">GIFT VOUCHERS</a>
    <a style="left:443px">REPLACEMENTS</a>
  </nav>

  <div class="abs search">Search
    <svg width="11" height="11" viewBox="0 0 11 11"><circle cx="6.5" cy="4.5" r="3.2" fill="none" stroke="#3a6ea8" stroke-width="1.4"/><line x1="4.2" y1="6.8" x2="1" y2="10" stroke="#3a6ea8" stroke-width="1.6"/></svg>
  </div>

  <div class="abs hero" role="img" aria-label="Banner photo: a loop of glowing orange, white and plum cotton ball lights against a pale wallpaper of bare trees"></div>
  <div class="abs slide-arrow" style="left:30px"><svg width="12" height="16" viewBox="0 0 12 16"><polyline points="10,1 3,8 10,15" fill="none" stroke="#fff" stroke-width="3"/></svg></div>
  <div class="abs slide-arrow" style="left:782px"><svg width="12" height="16" viewBox="0 0 12 16"><polyline points="2,1 9,8 2,15" fill="none" stroke="#fff" stroke-width="3"/></svg></div>

  <section class="abs feature" style="left:62px">
    <h2 class="section-title">LOREM IPSUM</h2>
    <p>Sed ut perspiciatis unde omnis iste natus error sit<br>voluptatem accusantium doloremque<br>laudantium, totam rem aperiam, eaque ipsa quae<br>ab illo inventore veritatis et quasi architecto<br>beatae vitae dicta sunt explicabo.</p>
  </section>
  <section class="abs feature" style="left:316px">
    <h2 class="section-title">LOREM IPSUM</h2>
    <p>Sed ut perspiciatis unde omnis iste natus error sit<br>voluptatem accusantium doloremque<br>laudantium, totam rem aperiam, eaque ipsa quae<br>ab illo inventore veritatis et quasi architecto<br>beatae vitae dicta sunt explicabo.</p>
  </section>
  <section class="abs feature" style="left:567px">
    <h2 class="section-title">LOREM IPSUM</h2>
    <p>Sed ut perspiciatis unde omnis iste natus error sit<br>voluptatem accusantium doloremque<br>laudantium, totam rem aperiam, eaque ipsa quae<br>ab illo inventore veritatis et quasi architecto<br>beatae vitae dicta sunt explicabo.</p>
  </section>

  <div class="abs products-title">
    <h2 class="section-title">OUR PRODUCTS</h2>
    <svg style="left:3px" width="10" height="16" viewBox="0 0 10 16"><polygon points="10,0 0,8 10,16" fill="#999"/></svg>
    <svg style="left:707px" width="10" height="16" viewBox="0 0 10 16"><polygon points="0,0 10,8 0,16" fill="#999"/></svg>
  </div>

  <div class="abs product" style="left:65px;top:682px;background:linear-gradient(160deg,#8e9aa6,#b86a84 55%,#8a6a3a)" role="img" aria-label="Product photo: cotton ball lights draped around vases"></div>
  <div class="abs product" style="left:186px;top:682px;background:linear-gradient(160deg,#e8e2da,#d9c8b2 60%,#c8a272)" role="img" aria-label="Product photo: pendant lamp with light balls on a patterned wall"></div>
  <div class="abs product" style="left:309px;top:682px;background:linear-gradient(160deg,#e6e0d6,#e8c49a 60%,#d99a5a)" role="img" aria-label="Product photo: colourful light balls scattered on a floor"></div>
  <div class="abs product" style="left:431px;top:682px;background:linear-gradient(160deg,#eef0f2,#ece2c0 60%,#e2e5e8)" role="img" aria-label="Product photo: light string above a white bed"></div>
  <div class="abs product" style="left:554px;top:682px;background:linear-gradient(160deg,#e6e6e6,#eea070 55%,#b0785a)" role="img" aria-label="Product photo: close-up of orange and teal light balls"></div>
  <div class="abs product" style="left:676px;top:682px;background:linear-gradient(160deg,#5a7ea6,#6a4a32 50%,#4a3222)" role="img" aria-label="Product photo: light balls and bunting on wooden boards"></div>

  <div class="abs product" style="left:65px;top:805px;background:linear-gradient(160deg,#9a8a7a,#c8708a 55%,#d89a5a)" role="img" aria-label="Product photo: light balls on wooden stairs"></div>
  <div class="abs product" style="left:186px;top:805px;background:linear-gradient(160deg,#1c2a3a,#4a7878 55%,#2a3a4a)" role="img" aria-label="Product photo: pile of dark teal light balls"></div>
  <div class="abs product" style="left:309px;top:805px;background:linear-gradient(160deg,#3a2e26,#6e5c48 55%,#2a221c)" role="img" aria-label="Product photo: dim hallway lit by a string of lights"></div>
  <div class="abs product" style="left:431px;top:805px;background:linear-gradient(160deg,#4a2218,#9a4a32 55%,#3a1a14)" role="img" aria-label="Product photo: glowing light balls in front of a brick fireplace"></div>
  <div class="abs product" style="left:554px;top:805px;background:linear-gradient(160deg,#6a88a6,#c4c8ce 55%,#9a9ea4)" role="img" aria-label="Product photo: child resting in bed under soft lights"></div>
  <div class="abs product" style="left:676px;top:805px;background:linear-gradient(160deg,#7a7a86,#a86a84 50%,#3a4656)" role="img" aria-label="Product photo: close-up of mixed colour light balls"></div>

  <section class="abs testimonials">
    <h2 class="section-title">TESTIMONIALS</h2>
    <blockquote class="quote" style="margin-top:23px">“Sed ut perspiciatis unde omnis iste natus error sit voluptatem accusantium<br>doloremque laudantium, totam rem aperiam, eaque ipsa quae ab illo inventore<br>veritatis et quasi architecto beatae vitae dicta sunt explicabo.”<cite>- Lorem Ipsum</cite></blockquote>
    <blockquote class="quote" style="margin-top:32px">“Sed ut perspiciatis unde omnis iste natus error sit voluptatem accusantium<br>doloremque laudantium, totam rem aperiam, eaque ipsa quae ab illo inventore<br>veritatis et quasi architecto beatae vitae dicta sunt explicabo.”<cite>- Lorem Ipsum</cite></blockquote>
  </section>

  <section class="abs subscribe">
    <h2 class="section-title">SUBSCRIBE NEWSLETTERS</h2>
    <p class="subscribe-intro">Subscribe to our newsletter and take advantage of our subscriber offers including<br>discount codes,product previews and our latest news.</p>
  </section>
  <div class="abs field" style="top:1032px">Name</div>
  <div class="abs field" style="top:1074px">Email</div>
  <div class="abs subscribe-btn">SUBSCRIBE</div>

  <footer class="abs footer">Copyrights © 2012. All Rights Reserved.</footer>
</div>
</body>
</html>
```